BRQ-Bramwell Resource Quarters LLC (Business Cards)

The attached design was selected as the logo for our company. I need to proceed on creating our business cards.

Tobias

Target Market(s)

This is a technology and Project Management company. The audience will be business decision makers of a diversity of companies.

Industry/Entity Type

Business

Font styles to use
Sans Serif
Script

Colors

Designer to choose colors to be used in the design.

```html
<!DOCTYPE html>
<html lang="en">
<head>
<meta charset="utf-8">
<title>Bramwell Resource Quarters – Business Card</title>
<link href="https://fonts.googleapis.com/css2?family=Alegreya:wght@400&family=Nunito+Sans:wght@300;400;600&display=swap" rel="stylesheet">
<style>
  :root {
    --brand-red: #920007;
    --rule-dark: #1f1f1f;
    --paper: #ffffff;
    --ink: #1a1a1a;
    --canvas: #ffffff;
  }
  * { margin: 0; padding: 0; box-sizing: border-box; }
  html, body {
    width: 1200px; height: 1000px; overflow: hidden;
    background: var(--canvas);
    font-family: "Nunito Sans", sans-serif;
  }
  .business-card {
    position: absolute; left: 167px; top: 236px;
    width: 890px; height: 508px;
    background: var(--paper);
    box-shadow: 1px 2px 4px rgba(0,0,0,0.35);
    overflow: hidden;
  }
  .header-band {
    position: absolute; left: 0; top: 0; width: 100%; height: 175px;
    background: var(--brand-red);
  }
  .header-rule {
    position: absolute; left: 0; top: 175px; width: 100%; height: 8px;
    background: var(--rule-dark);
  }
  .brand {
    position: absolute; left: 36px; top: 27px;
    display: flex; align-items: center;
  }
  .brand-circle {
    width: 116px; height: 116px; border-radius: 50%;
    background: var(--paper);
  }
  .brand-name {
    margin-left: 6px; margin-top: -4px;
    color: var(--paper);
    font-size: 21px; font-weight: 400; line-height: 24.5px;
    letter-spacing: 0.3px;
  }
  .holder-name {
    position: absolute; left: 37px; top: 198px;
    font-family: "Alegreya", serif; font-weight: 400;
    font-size: 43px; color: var(--brand-red);
    letter-spacing: 0.5px; line-height: 1;
  }
  .holder-position {
    position: absolute; left: 40px; top: 248px;
    font-size: 29px; font-weight: 400; color: var(--ink);
    line-height: 1; letter-spacing: 0.3px;
  }
  .contact-list {
    position: absolute; left: 36px; top: 294px; list-style: none;
  }
  .contact-item {
    display: flex; align-items: center; height: 47.5px;
    font-size: 25px; font-weight: 300; color: var(--ink);
  }
  .contact-icon { width: 35px; height: 35px; margin-right: 14px; flex: none; }
  .address {
    position: absolute; left: 481px; top: 304px;
    display: flex; align-items: flex-start;
    font-size: 25px; font-weight: 300; color: var(--ink); line-height: 34px;
  }
  .website {
    position: absolute; left: 481px; top: 443px;
    display: flex; align-items: center;
    font-size: 25px; font-weight: 300; color: var(--ink);
  }
  .address .contact-icon { margin-top: 0; margin-right: 13px; }
  .website .contact-icon { margin-right: 13px; }
</style>
</head>
<body>
  <div class="business-card">
    <div class="header-band"></div>
    <div class="header-rule"></div>

    <div class="brand">
      <div class="brand-circle"></div>
      <div class="brand-name">Bramwell<br>Resource<br>Quarters</div>
    </div>

    <h1 class="holder-name">TOBIAS RENHOLT</h1>
    <p class="holder-position">POSITION</p>

    <ul class="contact-list">
      <li class="contact-item">
        <svg class="contact-icon" viewBox="0 0 36 36"><circle cx="18" cy="18" r="18" fill="var(--brand-red)"/><text x="18" y="25" text-anchor="middle" font-size="21" font-family="Nunito Sans, sans-serif" font-weight="600" fill="#fff">@</text></svg>
        tobiasrenholt@mail.com
      </li>
      <li class="contact-item">
        <svg class="contact-icon" viewBox="0 0 36 36"><circle cx="18" cy="18" r="18" fill="var(--brand-red)"/><rect x="13" y="9" width="8" height="6" fill="#fff"/><rect x="9" y="15" width="18" height="8" rx="1" fill="#fff"/><rect x="12" y="21" width="12" height="6" fill="#fff" stroke="var(--brand-red)" stroke-width="1"/></svg>
        (000) 000-0000
      </li>
      <li class="contact-item">
        <svg class="contact-icon" viewBox="0 0 36 36"><circle cx="18" cy="18" r="18" fill="var(--brand-red)"/><rect x="12.5" y="8" width="11" height="20" rx="2" fill="none" stroke="#fff" stroke-width="2"/><circle cx="18" cy="25" r="1.2" fill="#fff"/></svg>
        (000) 000-0000
      </li>
      <li class="contact-item">
        <svg class="contact-icon" viewBox="0 0 36 36"><circle cx="18" cy="18" r="18" fill="var(--brand-red)"/><path d="M12 9 l4 0 l1.5 5 l-2.5 2 q2 4 5 6 l2-2.5 l5 1.5 l0 4 q-1 2 -4 1.5 q-8 -2 -12 -12 q-0.5 -4 1 -5.5z" fill="#fff"/></svg>
        (000) 000-0000
      </li>
    </ul>

    <div class="address">
      <svg class="contact-icon" viewBox="0 0 36 36"><circle cx="18" cy="18" r="18" fill="var(--brand-red)"/><path d="M18 28 q-7 -9 -7 -13 a7 7 0 0 1 14 0 q0 4 -7 13z" fill="#fff"/><circle cx="18" cy="15" r="2.6" fill="var(--brand-red)"/></svg>
      <span>Unit Building Name<br>Street. City Country</span>
    </div>

    <div class="website">
      <svg class="contact-icon" viewBox="0 0 36 36"><circle cx="18" cy="18" r="18" fill="var(--brand-red)"/><g fill="none" stroke="#fff" stroke-width="1.6"><circle cx="18" cy="18" r="10"/><ellipse cx="18" cy="18" rx="4.5" ry="10"/><line x1="8" y1="18" x2="28" y2="18"/><line x1="18" y1="8" x2="18" y2="28"/><line x1="10" y1="13" x2="26" y2="13"/><line x1="10" y1="23" x2="26" y2="23"/></g></svg>
      www.website.com
    </div>
  </div>
</body>
</html>
```